Business card for massage therapy company called Brook Fern Wellness

Need business card for massage therapy company called Brook Fern Wellness. Would like my logo on the front and the back of the card I have 3 options of logos and you can play with what looks better.

Would like this information displayed on the back of the card:

Marcus Ellery
Licensed Massage Therapist
321-555-0147
brookfern-example.com
brookfern_rest_

```html
<!DOCTYPE html>
<html lang="en">
<head>
<meta charset="utf-8">
<title>Brook Fern Wellness — Business Card</title>
<link href="https://fonts.googleapis.com/css2?family=Josefin+Sans:wght@300&family=Parisienne&family=Roboto:wght@400&display=swap" rel="stylesheet">
<style>
  :root {
    --backdrop: #3a3a3a;
    --card: #050505;
    --sage: #8a8a7a;
    --tan: #c49a7a;
    --ink: #f2f2f2;
    --rule: #d9d9d9;
  }
  * { margin: 0; padding: 0; box-sizing: border-box; }
  html, body { width: 1200px; height: 689px; overflow: hidden; }
  body {
    background: var(--backdrop);
    position: relative;
    font-family: "Roboto", Arial, sans-serif;
  }
  .card {
    position: absolute;
    top: 196px;
    width: 520px;
    height: 297px;
    background: var(--card);
    border-radius: 22px;
  }
  .card--front { left: 45px; }
  .card--back { left: 635px; }

  .brand {
    display: flex;
    align-items: center;
    gap: 14px;
    font-family: "Josefin Sans", Arial, sans-serif;
    font-weight: 300;
    color: var(--sage);
    text-transform: uppercase;
  }
  .brand__dot {
    flex: none;
    border: 1.5px solid var(--sage);
    border-radius: 50%;
  }
  .brand__name { line-height: 1.15; letter-spacing: 0.08em; }

  .card--front .brand {
    position: absolute;
    left: 0; right: 0; top: 0; bottom: 0;
    justify-content: center;
  }
  .card--front .brand__dot { width: 62px; height: 62px; }
  .card--front .brand__name { font-size: 34px; }

  .card--back .brand {
    position: absolute;
    right: 34px;
    top: 40px;
  }
  .card--back .brand__dot { width: 40px; height: 40px; }
  .card--back .brand__name { font-size: 19px; }

  .rule {
    position: absolute;
    height: 1px;
    background: var(--rule);
  }
  .rule--top { left: 200px; right: 30px; top: 120px; }
  .rule--mid { left: 36px; width: 200px; top: 196px; }

  .person {
    position: absolute;
    left: 36px;
    top: 130px;
  }
  .person__name {
    font-family: "Parisienne", cursive;
    font-size: 34px;
    color: var(--sage);
    line-height: 1;
  }
  .person__role {
    margin-top: 6px;
    font-size: 14px;
    color: var(--tan);
  }

  .contacts {
    position: absolute;
    left: 36px;
    top: 210px;
    list-style: none;
  }
  .contacts__item {
    display: flex;
    align-items: center;
    gap: 10px;
    height: 22px;
    font-size: 14px;
    color: var(--ink);
  }
  .contacts__icon { width: 14px; height: 14px; flex: none; }
</style>
</head>
<body>
  <section class="card card--front" aria-label="Card front">
    <div class="brand">
      <span class="brand__dot"></span>
      <span class="brand__name">Brook Fern<br>Wellness</span>
    </div>
  </section>

  <section class="card card--back" aria-label="Card back">
    <div class="brand">
      <span class="brand__dot"></span>
      <span class="brand__name">Brook Fern<br>Wellness</span>
    </div>
    <div class="rule rule--top"></div>

    <div class="person">
      <p class="person__name">Marcus Ellery</p>
      <p class="person__role">Licensed Massage Therapist</p>
    </div>
    <div class="rule rule--mid"></div>

    <ul class="contacts">
      <li class="contacts__item">
        <svg class="contacts__icon" viewBox="0 0 24 24" fill="none" stroke="#9a9a9a" stroke-width="2" stroke-linecap="round" stroke-linejoin="round"><path d="M22 16.9v3a2 2 0 0 1-2.2 2 19.8 19.8 0 0 1-8.6-3.1 19.5 19.5 0 0 1-6-6A19.8 19.8 0 0 1 2.1 4.2 2 2 0 0 1 4.1 2h3a2 2 0 0 1 2 1.7c.1 1 .4 1.9.7 2.8a2 2 0 0 1-.5 2.1L8 9.9a16 16 0 0 0 6 6l1.3-1.3a2 2 0 0 1 2.1-.4c.9.3 1.8.6 2.8.7a2 2 0 0 1 1.7 2z"/></svg>
        321-555-0147
      </li>
      <li class="contacts__item">
        <svg class="contacts__icon" viewBox="0 0 24 24" fill="none" stroke="#9a9a9a" stroke-width="2"><circle cx="12" cy="12" r="10"/><path d="M2 12h20M12 2a15 15 0 0 1 0 20M12 2a15 15 0 0 0 0 20"/></svg>
        brookfern-example.com
      </li>
      <li class="contacts__item">
        <svg class="contacts__icon" viewBox="0 0 24 24" fill="none" stroke="#9a9a9a" stroke-width="2"><circle cx="12" cy="12" r="9"/></svg>
        brookfern_rest_
      </li>
    </ul>
  </section>
</body>
</html>
```